DM - management consultant

Business card - contemporary design

Front info
Dorian Maples

(Address not necessary)
PO Box 7386
Belmont, CA 94002

(650) 555-0143
dm@dorianmapl.es

Twitter: dmq527
Facebook: /Dorian.Maples
Profile: /in/dorianmaples

Back or Front
www.dorianmaples.net
Facilitation & coaching, change management, strategic partnerships, business improvement

Target Market(s)

High tech businesses - mostly startups in Silicon Valley

Industry/Entity Type

Business

Font styles to use
Sans Serif

Colors

Designer to choose colors to be used in the design.

```html
<!DOCTYPE html>
<html lang="en">
<head>
<meta charset="utf-8">
<title>Dorian Maples – Business Card</title>
<link rel="stylesheet" href="https://fonts.googleapis.com/css2?family=Open+Sans:wght@300;400;700&display=swap">
<style>
  :root {
    --canvas-bg: #e9e7e3;
    --card-white: #f4f5f5;
    --card-grey: #6a6d73;
    --ink-grey: #5d6066;
    --accent-orange: #e8962a;
    --back-text: #d9dbde;
  }
  * { margin: 0; padding: 0; box-sizing: border-box; }
  html, body {
    width: 1200px;
    height: 617px;
    overflow: hidden;
    background: var(--canvas-bg);
    font-family: "Open Sans", sans-serif;
  }
  .canvas {
    position: relative;
    width: 1200px;
    height: 617px;
    display: flex;
    align-items: center;
    justify-content: center;
    gap: 40px;
  }
  .card {
    width: 500px;
    height: 286px;
    box-shadow: 0 6px 18px rgba(0, 0, 0, 0.18);
  }
  .card-front {
    background: linear-gradient(160deg, #ffffff 0%, var(--card-white) 100%);
    padding: 34px 38px;
    color: var(--ink-grey);
  }
  .name {
    font-weight: 700;
    font-size: 26px;
    line-height: 1.1;
    color: var(--ink-grey);
  }
  .title {
    font-size: 17px;
    color: var(--accent-orange);
    margin-top: 2px;
  }
  .contact-list {
    list-style: none;
    margin-top: 26px;
    font-size: 16px;
    line-height: 1.4;
  }
  .contact-label {
    color: var(--accent-orange);
  }
  .card-back {
    background: var(--card-grey);
    padding: 40px 42px;
    color: var(--back-text);
    font-weight: 300;
  }
  .back-block {
    display: inline-block;
  }
  .services {
    font-size: 19px;
    line-height: 1.45;
  }
  .divider {
    color: var(--back-text);
    opacity: 0.8;
  }
  .website {
    margin-top: 18px;
    font-size: 18px;
    text-align: center;
    color: var(--accent-orange);
  }
  .website .tld {
    color: var(--back-text);
  }
</style>
</head>
<body>
<main class="canvas">
  <section class="card card-front" aria-label="Card front">
    <h1 class="name">Dorian Maples</h1>
    <p class="title">Executive Advisor</p>
    <ul class="contact-list">
      <li><span class="contact-label">Phone:</span> (650) 555-0143</li>
      <li><span class="contact-label">E-mail:</span> dm@dorianmapl.es</li>
      <li><span class="contact-label">Profile:</span> /in/dorianmaples</li>
      <li><span class="contact-label">Web:</span> www.dorianmaples.net</li>
    </ul>
  </section>
  <section class="card card-back" aria-label="Card back">
    <div class="back-block">
      <p class="services">Facilitation &amp; coaching <span class="divider">|</span> change management<br>strategic partnerships <span class="divider">|</span> business improvement</p>
      <p class="website">www.dorianmaples<span class="tld">.net</span></p>
    </div>
  </section>
</main>
</body>
</html>
```